Poster design for Non-Profit Harbor Pathways

Harbor Pathways is a not-for-profit providing disability services to improve the lives of the people we serve. We are holding an internal convention with staff focusing on improving what we already do well. The title of the event and ongoing effort will be ‘Ventus Aperta’, with a sub-title of ‘Focusing on our Strengths’.

Target Market(s)

Our employees

Industry/Entity Type

Non Profit

Font styles to use
Serif

Requirements
Must have
• • Be A0 size
• • Include the title ‘Ventus Aperta’
• • Include the sub-title ‘ Focusing on our Strengths’
• • Include the Harbor Pathways Logo
• • A colour scheme that ties in to our logo
Nice to have
• A bold, minimalist design with clear lettering. Refer to the files inspiration 1 and 2. Also I will upload a brochure we had designed recently. Please ignore our website for design features as it is outdated.
Should not have
• Too many photos.

```html
<!DOCTYPE html>
<html lang="en">
<head>
<meta charset="utf-8">
<title>Ventus Aperta — Focusing On Our Strengths</title>
<link rel="stylesheet" href="https://fonts.googleapis.com/css2?family=Pinyon+Script&family=Libre+Baskerville:wght@700&family=Cormorant+Garamond:wght@500&family=Playfair+Display:wght@700&display=swap">
<style>
  :root {
    --violet-deep: #6a2f8e;
    --violet-mid: #8347a8;
    --violet-glow: #9a5fbf;
    --ink-light: #ffffff;
    --ornament-tone: #e7dcef;
  }
  html, body {
    margin: 0;
    padding: 0;
    width: 849px;
    height: 1200px;
    overflow: hidden;
  }
  .poster {
    position: relative;
    width: 849px;
    height: 1200px;
    overflow: hidden;
    background:
      radial-gradient(ellipse 70% 55% at 50% 40%, var(--violet-glow) 0%, var(--violet-mid) 45%, var(--violet-deep) 100%);
    color: var(--ink-light);
    text-align: center;
  }
  .poster > * {
    position: absolute;
    left: 0;
    right: 0;
    margin: 0;
  }
  .title-script {
    top: 40px;
    font-family: "Pinyon Script", cursive;
    font-weight: 400;
    font-size: 172px;
    line-height: 1;
  }
  .title-bold {
    top: 280px;
    font-family: "Libre Baskerville", serif;
    font-weight: 700;
    font-size: 92px;
    line-height: 1;
  }
  .divider-flourish {
    top: 405px;
    left: 235px;
    right: auto;
    width: 380px;
    height: 46px;
    border-radius: 23px;
    background: linear-gradient(90deg, transparent 0%, var(--ornament-tone) 20%, var(--ornament-tone) 80%, transparent 100%);
    opacity: 0.55;
  }
  .subtitle-lead {
    top: 500px;
    font-family: "Cormorant Garamond", serif;
    font-weight: 500;
    font-size: 92px;
    letter-spacing: 18px;
    line-height: 1;
    padding-left: 18px;
  }
  .subtitle-joiner {
    top: 605px;
    font-family: "Pinyon Script", cursive;
    font-size: 96px;
    line-height: 1.1;
    letter-spacing: 10px;
    color: transparent;
    -webkit-text-stroke: 2px var(--ink-light);
  }
  .subtitle-key {
    top: 725px;
    font-family: "Playfair Display", serif;
    font-weight: 700;
    font-size: 66px;
    letter-spacing: 12px;
    line-height: 1;
    padding-left: 12px;
  }
  .org-name {
    top: 895px;
    font-family: "Libre Baskerville", serif;
    font-weight: 700;
    font-size: 46px;
    letter-spacing: 2px;
    line-height: 1;
  }
</style>
</head>
<body>
  <main class="poster">
    <h1 class="title-script">Ventus</h1>
    <p class="title-bold">Aperta</p>
    <div class="divider-flourish" role="img" aria-label="Decorative scroll flourish divider"></div>
    <p class="subtitle-lead">Focusing</p>
    <p class="subtitle-joiner">On Our</p>
    <p class="subtitle-key">STRENGTHS!</p>
    <p class="org-name">Harbor Pathways</p>
  </main>
</body>
</html>
```